Simple Easy - Taekwondo brochure

I have the content and an idea of the layout I want. I need it to look nice and sharp.

It's a sided 8.5x11 colored brochure

please feel free to move things around and use the images provided

my website is www.plovenhart.net if you need an understanding of what the business is about.

all text content is on the website. please be creative!

Target Market(s)

Mothers...must by family friendly because it's for mothers to bring their kids.

Industry/Entity Type

Martial Art

Other font styles liked:
• Lato

```html
<!DOCTYPE html>
<html lang="en">
<head>
<meta charset="utf-8">
<title>Plovenhart Taekwondo – Trifold Brochure</title>
<link rel="stylesheet" href="https://fonts.googleapis.com/css2?family=Lato:wght@400;700;900&family=Oswald:wght@600&family=Lora:wght@400&family=Bungee&display=swap">
<style>
:root{
  --stage:#c99a9c;
  --red:#c8202a;
  --blue:#1f6fc4;
  --ink:#2b2b2b;
  --dark:#262626;
  --paper:#f1f1f1;
  --white:#ffffff;
}
*{box-sizing:border-box;margin:0;padding:0}
html,body{width:1200px;height:1200px;overflow:hidden;background:var(--stage)}
.brochure{position:absolute;left:50px;top:175px;width:1100px;height:850px;background:var(--paper);overflow:hidden;box-shadow:0 10px 30px rgba(0,0,0,.25);font-family:"Lato",sans-serif;color:var(--ink)}
.panel{position:absolute;top:0;height:850px;width:366.67px}
.panel--bio{left:0;background:linear-gradient(180deg,#f6f6f6,#e6e6e6)}
.panel--offer{left:366.67px;background:linear-gradient(180deg,#fafafa,#ececec);border-left:1px solid #d6d6d6}
.panel--cover{left:733.33px;background:linear-gradient(180deg,#5a5a5a,#3a3a3a)}
.panel--overlay{background:none}
.shapes{position:absolute;inset:0;width:1100px;height:850px}
.tab{position:absolute;top:34px;background:var(--red);color:var(--white);font-weight:700;font-size:13px;padding:4px 14px 4px 12px;clip-path:polygon(0 0,100% 0,92% 100%,0 100%)}
.bio-text,.quote{position:absolute;font-size:10.3px;line-height:1.42;text-align:justify;color:#333}
.bio-text{left:28px;top:68px;width:310px}
.bio-text p{margin-bottom:9px}
.quote{left:24px;top:68px;width:318px}
.belt-photo{position:absolute;left:0;top:540px;width:366.67px;height:260px;background:linear-gradient(180deg,rgba(230,230,230,0) 0%,#d8d8d8 30%,#9a9a9a 70%,#3a3a3a 100%)}
.offer-title{position:absolute;left:0;width:366.67px;top:262px;text-align:center;font-family:"Lora",serif;font-weight:400;font-size:19px;color:#333}
.offer-box{position:absolute;left:110px;top:298px;width:146px;height:90px;border:2px solid var(--blue);border-radius:8px;background:var(--white);text-align:center;padding-top:6px}
.offer-box__big{font-family:"Oswald",sans-serif;font-size:34px;line-height:1;color:var(--red)}
.offer-box__small{font-size:11px;color:var(--blue);line-height:1.25;margin-top:6px;letter-spacing:.3px}
.map{position:absolute;left:465px;top:455px;width:170px;height:190px}
.address,.callout,.url{position:absolute;color:var(--white)}
.address,.callout{left:366.67px;width:366.67px;text-align:center;font-size:11.5px;display:flex;align-items:center;justify-content:center;gap:6px}
.address{top:742px}
.callout{top:811px;font-weight:700}
.url{font-size:10.5px;letter-spacing:3px;font-weight:700}
.url--bio{left:70px;top:820px}
.url--cover{left:800px;top:815px}
.coach-photo{position:absolute;left:10px;top:60px;width:250px;height:500px;background:linear-gradient(160deg,#cfcfcf 0%,#f4f4f4 40%,#bdbdbd 75%,#5a5a5a 100%);border-radius:110px 110px 0 0}
.brand{position:absolute;left:250px;top:20px;width:110px;text-align:center}
.brand__mark{width:84px;height:84px;border-radius:50%;background:var(--white);margin:0 auto 10px}
.brand__name{font-weight:900;font-size:11px;line-height:1.35;color:var(--white);letter-spacing:.5px}
.headline{position:absolute;left:0;width:366.67px;top:608px;text-align:center;font-family:"Bungee",sans-serif;font-weight:400;font-size:33px;line-height:1.25;color:var(--white)}
.headline__accent{color:var(--red)}
</style>
</head>
<body>
<main class="brochure">
  <section class="panel panel--bio">
    <div class="belt-photo" role="img" aria-label="Photo of hands holding a black belt over a white uniform"></div>
    <div class="tab">Master Dan</div>
    <div class="bio-text">
      <p>Daniel Rhee (Master Dan) is the owner and head instructor at Plovenhart Taekwondo. Master Dan is a Dojang Council certified 3rd degree Black Belt, the overseeing authority of all Black Belts in the world, working with the Global Taekwondo Union (GTU); it also oversees taekwondo at international games. In 1992, at the age of 8, Master Dan began training under Grand Master Verano, who achieved the level of 8th Dan in taekwondo under the Allied Taekwondo League (ATL). When Master Dan entered middle school and then high school, his years of taekwondo training became invaluable as he participated in wrestling, track, and hockey.</p>
      <p>Master Dan continued his taekwondo training after high school, and in 2007 began training under Grand Master Oh, who has achieved the level of 6th Dan in Taekwondo. Grand Master Oh was also a distinguished member of a national team that competed around the world.</p>
      <p>While attending Harlow University, Master Dan joined the university's Taekwondo Team. Upon graduating in 2008, he was invited to become the team's Assistant Coach. Because of his exceptional skill and his ability to positively influence and motivate the team, the university selected him to lead as coach. Master Dan served as Head Coach of the team from 2010–2013.</p>
      <p>In 2013, Master Dan began training under Grand Master Baek, a 9th Dan in Taekwondo. Master Dan currently trains under Grand Master Baek.</p>
    </div>
  </section>

  <section class="panel panel--offer">
    <div class="tab">Nora K.</div>
    <p class="quote">I started taking classes with Master Dan a little over 3 years ago. As the newest member of the class, I was shy and unsure of myself. However, I quickly overcame those feelings because Master Dan is a natural teacher. Paired with his passion for the sport, his gift for teaching makes him one of the best coaches I have encountered. I have seen him work with both children and adults and his manner is unfailingly supportive and encouraging. As a teacher myself, I see how he tailors his teaching style to each student and I hope to follow his example in my classroom. I am thankful that my first experience with taekwondo has been through Master Dan's class.</p>
    <h2 class="offer-title">Special Offer</h2>
    <div class="offer-box">
      <div class="offer-box__big">50% OFF</div>
      <div class="offer-box__small">TRIAL LESSONS AND<br>GET A FREE T-SHIRT!</div>
    </div>
  </section>

  <section class="panel panel--cover">
    <div class="coach-photo" role="img" aria-label="Photo of the head instructor in a white uniform, arms crossed"></div>
  </section>

  <svg class="shapes" viewBox="0 0 1100 850" aria-hidden="true">
    <polygon points="733,0 1100,0 1100,40 733,150" fill="#c8202a"/>
    <polygon points="733,150 1100,40 1100,48 733,158" fill="#ffffff"/>
    <polygon points="733,158 1100,48 1100,58 733,168" fill="#1f6fc4"/>
    <polygon points="366.67,722 1100,470 1100,850 366.67,850" fill="#262626"/>
    <polygon points="366.67,700 1100,448 1100,458 366.67,710" fill="#c8202a"/>
    <polygon points="366.67,710 1100,458 1100,464 366.67,716" fill="#ffffff"/>
    <polygon points="366.67,716 1100,464 1100,472 366.67,724" fill="#1f6fc4"/>
    <polygon points="0,806 366.67,796 366.67,850 0,850" fill="#c8202a"/>
    <polygon points="366.67,796 733.33,796 733.33,850 366.67,850" fill="#c8202a"/>
    <polygon points="733.33,800 1090,790 1100,850 733.33,850" fill="#c8202a"/>
    <polygon points="1060,792 1100,790 1100,850 1090,850" fill="#1f6fc4"/>
    <line x1="733.33" y1="0" x2="733.33" y2="850" stroke="#1b1b1b" stroke-width="1"/>
  </svg>

  <svg class="map" viewBox="0 0 170 190" role="img" aria-label="Street map showing the studio location">
    <polygon points="85,4 164,48 164,142 85,186 6,142 6,48" fill="#1f6fc4"/>
    <polygon points="85,12 157,52 157,138 85,178 13,138 13,52" fill="#ffffff"/>
    <polygon points="85,18 151,55 151,135 85,172 19,135 19,55" fill="#dedcd6"/>
  </svg>

  <p class="address">
    <svg width="9" height="12" viewBox="0 0 8 11" aria-hidden="true"><path d="M0 4a4 4 0 0 1 8 0c0 3-4 7-4 7S0 7 0 4z" fill="#fff"/></svg>
    <span>218 Linden Road, Marlow Heights, PA 19000</span>
  </p>
  <p class="callout">
    <span>Call us today!</span>
    <svg width="14" height="14" viewBox="0 0 14 14" aria-hidden="true"><circle cx="7" cy="7" r="6.2" fill="none" stroke="#fff" stroke-width="1.3"/><path d="M4.5 4.3q0 5.2 5.2 5.2l.9-1.4-1.6-1-1 .8q-1.7-.7-2.5-2.5l.8-1-1-1.6z" fill="#fff"/></svg>
    <span>555-014-2290</span>
  </p>

  <p class="url url--bio">www.plovenhart.net</p>
  <p class="url url--cover">www.plovenhart.net</p>

  <div class="panel panel--cover panel--overlay">
    <div class="brand">
      <div class="brand__mark"></div>
      <p class="brand__name">PLOVENHART<br>TAEKWONDO</p>
    </div>
    <h1 class="headline">FOCUS<br><span class="headline__accent">YOUR CHILD'S</span><br>POTENTIAL</h1>
  </div>
</main>
</body>
</html>
```